Gestaltung Deutschlandfahne
Zielgruppe
Korvexa Verkäufer / Korvexa Käufer
Aufgabenstellung
Gestaltung einer Deutschlandfahne.
Frei in der Gestaltung nach vorgegebener Skizze

```html
<!DOCTYPE html>
<html lang="de">
<head>
<meta charset="utf-8">
<title>Deutschlandfahne 2024</title>
<link rel="stylesheet" href="https://fonts.googleapis.com/css2?family=Open+Sans:wght@700&display=swap">
<style>
  :root {
    --page-bg: #e8eaed;
    --flag-black: #050608;
    --flag-red: #e01e1e;
    --flag-gold: #f6ca1c;
    --star-gold: #fbc21b;
    --star-light: #fde047;
    --line-white: #ffffff;
  }
  * { margin: 0; padding: 0; box-sizing: border-box; }
  html, body {
    width: 882px;
    height: 1200px;
    overflow: hidden;
    background: var(--page-bg);
  }
  .flag {
    position: absolute;
    left: 0;
    top: 337px;
    width: 882px;
    height: 526px;
    overflow: hidden;
  }
  .band { position: absolute; left: 0; width: 100%; }
  .band--black { top: 0; height: 175px; background: var(--flag-black); }
  .band--red { top: 175px; height: 175px; background: var(--flag-red); }
  .band--gold { top: 350px; height: 176px; background: var(--flag-gold); }

  .ball-art {
    position: absolute;
    left: 497px;
    top: 96px;
    width: 448px;
    height: 448px;
    border-radius: 50%;
    background: radial-gradient(circle at 45% 40%, rgba(255,255,255,0.55), rgba(255,255,255,0.25) 70%, rgba(255,255,255,0.1));
    border: 5px solid var(--line-white);
  }

  .frame {
    position: absolute;
    left: 0;
    top: 0;
    width: 882px;
    height: 526px;
  }

  .stars {
    position: absolute;
    left: 259px;
    top: 34px;
    display: flex;
    gap: 27px;
  }
  .star { width: 70px; height: 68px; }

  .year {
    position: absolute;
    left: 96px;
    top: 307px;
    font-family: "Open Sans", sans-serif;
    font-weight: 700;
    font-size: 160px;
    line-height: 1;
    color: var(--line-white);
    letter-spacing: -2px;
    transform: rotate(-10deg);
    transform-origin: left bottom;
  }
</style>
</head>
<body>
  <main class="flag">
    <div class="band band--black"></div>
    <div class="band band--red"></div>
    <div class="band band--gold"></div>

    <div class="ball-art" role="img" aria-label="Illustration eines Fußballs in Weiß, durch den die Fahnenfarben scheinen"></div>

    <svg class="frame" viewBox="0 0 882 526" aria-hidden="true">
      <g fill="none" stroke="var(--line-white)" stroke-width="1.2">
        <polyline points="238,61 60,61 60,465 84,465"/>
        <polyline points="643,61 821,61 821,465 184,465"/>
      </g>
    </svg>

    <div class="stars" aria-hidden="true">
      <svg class="star" viewBox="0 0 70 68"><polygon points="35,0 43,25 70,25 48,41 56,68 35,51 14,68 22,41 0,25 27,25" fill="var(--star-gold)"/><polygon points="35,0 27,25 0,25 22,41 14,68 35,51" fill="var(--star-light)"/></svg>
      <svg class="star" viewBox="0 0 70 68"><polygon points="35,0 43,25 70,25 48,41 56,68 35,51 14,68 22,41 0,25 27,25" fill="var(--star-gold)"/><polygon points="35,0 27,25 0,25 22,41 14,68 35,51" fill="var(--star-light)"/></svg>
      <svg class="star" viewBox="0 0 70 68"><polygon points="35,0 43,25 70,25 48,41 56,68 35,51 14,68 22,41 0,25 27,25" fill="var(--star-gold)"/><polygon points="35,0 27,25 0,25 22,41 14,68 35,51" fill="var(--star-light)"/></svg>
      <svg class="star" viewBox="0 0 70 68"><polygon points="35,0 43,25 70,25 48,41 56,68 35,51 14,68 22,41 0,25 27,25" fill="var(--star-gold)"/><polygon points="35,0 27,25 0,25 22,41 14,68 35,51" fill="var(--star-light)"/></svg>
    </div>

    <p class="year">2024</p>
  </main>
</body>
</html>
```